Revamp Current Website From 2012 TO 2018

We need a ravamp to our current website. I prefer a professional corporate modern feel to it.

My Current Website is www.brightlanepromoworks.biz. Please redesign the homepage and the /certs page first....see attached document for specific instructions..

There is a lot of content at the bottom but maybe we can shorten that by using titles and a pop up of the details or something so it doesnt take too mcuh space...or maybe a red more hyperlink to see the rest of info in pop up or something or new page...

Target Market(s)

B2B, business owners, website owners, marketing companies.

Industry/Entity Type

Promotional Product

Number of Pages Required

2 page

Colors

Designer to choose colors to be used in the design.

Requirements
Must have
• Please keep in mind logo mock up I am working on that looks beautiful on dark background for header...see attached for logo
• Must use existing content I hope your marketing mind comes in to play when designing the website.
• Must have all my content provided on each page...
Nice to have
• similiar color scheme...
Should not have
• I dont like using templates because usually hard to expand on design in future so Prefer full custom designs
• Please no templates

```html
<!DOCTYPE html>
<html lang="en">
<head>
<meta charset="utf-8">
<title>Brightlane Promo Works – Unlimited Incentives</title>
<link rel="stylesheet" href="https://fonts.googleapis.com/css2?family=Raleway:wght@300;400;500;600&family=Open+Sans:wght@400;600;700&display=swap">
<style>
:root{
  --navy:#0c1a3a;
  --navy-deep:#071026;
  --blue:#0a5fd6;
  --blue-bright:#1577e8;
  --violet:#3b2f8f;
  --ink:#2c2f36;
  --muted:#6b7078;
  --light:#f4f5f7;
  --white:#ffffff;
  --red:#e8322f;
  --footer:#0b0f1a;
}
*{box-sizing:border-box;margin:0;padding:0}
html,body{width:1200px;height:4721px;overflow:hidden}
body{font-family:"Open Sans",Arial,sans-serif;color:var(--ink);background:var(--white);position:relative}
a{color:inherit;text-decoration:none}
section,header,footer{position:absolute;left:0;width:1200px;overflow:hidden}
.heading{font-family:"Raleway",Arial,sans-serif;font-weight:300}

/* hero */
.hero{top:0;height:592px;background:var(--navy)}
.hero-photo{position:absolute;inset:0;background:linear-gradient(100deg,#2a2ea8 0%,#4b3fb8 38%,#8a5fa0 62%,#d88b6a 85%,#f0b07a 100%)}
.hero-shade{position:absolute;inset:0;background:linear-gradient(90deg,rgba(8,20,70,.55) 0%,rgba(8,20,70,0) 60%)}
.topnav{position:absolute;top:24px;left:100px;right:100px;display:flex;align-items:center;justify-content:space-between}
.brand{display:flex;align-items:center;gap:10px;font-family:"Raleway",sans-serif;font-weight:600;font-size:17px;color:var(--white);letter-spacing:.5px}
.brand-dot{width:26px;height:26px;background:var(--blue-bright)}
.menu{display:flex;gap:30px;font-size:12.5px;color:rgba(255,255,255,.85)}
.menu .active{color:#8fc0ff}
.contact-line{position:absolute;top:92px;left:100px;font-size:11.5px;color:rgba(255,255,255,.9);display:flex;gap:18px}
.hero-title{position:absolute;top:254px;left:100px;font-size:34px;line-height:1.3;color:var(--white)}
.hero-actions{position:absolute;top:402px;left:100px;display:flex;gap:18px}
.btn{display:inline-block;height:36px;line-height:36px;padding:0 26px;font-size:12px;border-radius:2px}
.btn-white{background:var(--white);color:var(--blue)}
.btn-blue{background:var(--blue-bright);color:var(--white)}

/* incentives */
.incentives{top:592px;height:542px;background:var(--white)}
.incentives h2{position:absolute;top:55px;width:100%;text-align:center;font-size:26px;color:#3d4250}
.cards{position:absolute;top:142px;left:100px;width:1000px;height:337px;display:flex}
.card{flex:1;position:relative;color:var(--white);text-align:center}
.card .img{position:absolute;inset:0}
.card .veil{position:absolute;inset:0;background:rgba(0,0,0,.28)}
.card h3{position:relative;margin-top:152px;font-family:"Raleway",sans-serif;font-weight:600;font-size:14px;padding:0 18px;line-height:1.3}
.card p{position:relative;font-size:10.5px;line-height:1.6;margin-top:10px;padding:0 24px}
.card .more{position:relative;display:block;margin-top:14px;font-size:10.5px}
.c1 .img{background:linear-gradient(180deg,#4a6a86,#2c3e4f)}
.c1 h3{margin-top:110px}
.c2 .img{background:linear-gradient(180deg,#8fb4d8,#3f7aa8)}
.c3 .img{background:linear-gradient(180deg,#c89a70,#6a4a36)}
.c4 .img{background:linear-gradient(180deg,#9a7a6a,#3e2f2c)}
.c5 .img{background:linear-gradient(180deg,#b89a8c,#7c4b58)}

/* stats */
.stats{top:1134px;height:183px;background:linear-gradient(90deg,#0a56c8,#1577e8 55%,#0a56c8)}
.stat{position:absolute;top:50px;width:200px;text-align:center;color:var(--white)}
.stat strong{display:block;font-family:"Raleway",sans-serif;font-weight:400;font-size:34px}
.stat span{display:block;font-size:11px;margin-top:10px}

/* wing */
.wing{top:1317px;height:497px}
.wing-photo{position:absolute;inset:0;background:linear-gradient(180deg,#2a3a5c 0%,#7b5a6a 40%,#c9825e 62%,#6a5550 80%,#2e2a33 100%)}
.wing-copy{position:absolute;top:238px;left:520px;width:560px;color:var(--white)}
.wing-copy h2{font-size:22px;line-height:1.35}
.wing-copy p{font-size:11px;line-height:1.65;margin-top:16px}
.wing-copy .strong{font-weight:700;margin-top:12px}
.wing-copy .btn{margin-top:18px;background:var(--white);color:var(--blue);height:34px;line-height:34px}

/* plug in */
.plugin{top:1814px;height:517px;background:var(--light)}
.plugin h2{position:absolute;top:82px;left:100px;font-size:25px;color:#3d4250}
.tile{position:absolute;width:330px}
.tile h3{font-size:13px;font-weight:700;color:var(--blue)}
.tile p{font-size:10.5px;line-height:1.65;margin-top:8px;color:var(--muted)}
.phone-mock{position:absolute;top:30px;left:850px;width:240px;height:460px;border-radius:36px;background:#e9eaee;border:2px solid #d2d4da}
.phone-screen{position:absolute;top:60px;left:14px;right:14px;bottom:60px;background:linear-gradient(180deg,#2a1a5a,#b0305a 55%,#e08a3a)}

/* distribution */
.distribution{top:2331px;height:346px;background:linear-gradient(90deg,#0a4fc0,#1370e0 50%,#0a4fc0);color:var(--white)}
.distribution h2{position:absolute;top:48px;width:100%;text-align:center;font-size:24px}
.channel{position:absolute;top:135px;width:220px;text-align:center}
.channel svg{display:block;margin:0 auto}
.channel h3{font-size:13px;font-weight:700;margin-top:14px}
.channel p{font-size:10.5px;line-height:1.6;margin-top:8px}

/* gift */
.gift{top:2677px;height:426px}
.gift-photo{position:absolute;inset:0;background:linear-gradient(90deg,#1a1410 0%,#3a2a20 45%,#4a3a30 70%,#1d6a78 88%,#152128 100%)}
.gift-copy{position:absolute;top:164px;left:100px;width:600px;color:var(--white)}
.gift-copy h2{font-size:22px;line-height:1.35}
.gift-copy p{font-size:10.5px;line-height:1.65;margin-top:14px}
.gift-actions{display:flex;align-items:center;gap:22px;margin-top:20px}
.gift-actions .btn{background:var(--blue-bright);color:var(--white);height:32px;line-height:32px}
.gift-actions a.link{font-size:10.5px;color:#8fc0ff}

/* support cards */
.support{top:3103px;height:614px;background:#111318}
.scard{position:absolute;top:47px;width:313px;height:504px}
.scard .img{position:absolute;inset:0}
.s1 .img{background:linear-gradient(180deg,#2a2e36,#4a4e58)}
.s2 .img{background:linear-gradient(180deg,#6a6e74,#2e3036)}
.s3 .img{background:linear-gradient(180deg,#8a8c90,#3a3c42)}
.s1 .panel{position:absolute;left:0;right:0;top:205px;bottom:0;background:var(--blue-bright);color:var(--white);text-align:center;padding:28px 26px}
.s1 .panel h3{font-size:12.5px;line-height:1.45;font-weight:700}
.s1 .panel p{font-size:10.5px;line-height:1.6;margin-top:14px}
.s1 .panel a{display:block;font-size:11px;font-weight:700;margin-top:12px}
.scard .caption{position:absolute;left:0;right:0;bottom:40px;text-align:center;color:var(--white);font-size:11.5px;font-weight:700;padding:0 20px}

/* sales */
.sales{top:3717px;height:520px}
.sales-photo{position:absolute;inset:0;background:linear-gradient(90deg,#c42a26 0%,#e2524a 18%,#f3e7e4 40%,#f6f6f6 60%,#f2f2f2 100%)}
.sales-copy{position:absolute;top:250px;right:95px;text-align:right}
.sales-copy h2{font-size:21px;line-height:1.35;color:#3d4250}
.sales-links{display:flex;gap:30px;justify-content:flex-end;margin-top:14px;font-size:10.5px;color:var(--blue)}

/* reseller cta */
.reseller{top:4237px;height:204px;background:var(--navy)}
.reseller-photo{position:absolute;top:0;right:0;width:400px;height:100%;background:linear-gradient(90deg,#0c1a3a 0%,#5a6a82 35%,#c9b5a5 70%,#e8ddd3 100%)}
.reseller h2{position:absolute;top:66px;left:100px;width:760px;font-size:21px;line-height:1.35;color:var(--white)}
.reseller a{position:absolute;top:148px;left:100px;font-size:10.5px;color:#8fc0ff}

/* footer */
.site-footer{top:4441px;height:280px;background:var(--footer);color:#9aa0ab}
.fcol{position:absolute;top:52px;font-size:10.5px;line-height:1.75}
.fcol h4{font-size:10.5px;font-weight:400;color:var(--white)}
.fcol li{list-style:none}
.fcol .ico{display:inline-block;width:9px;height:9px;border-radius:50%;background:#4a5262;margin-right:6px;vertical-align:middle}
.copyright{position:absolute;left:0;right:0;bottom:0;height:36px;line-height:36px;text-align:center;font-size:10px;border-top:1px solid #1f2430}
</style>
</head>
<body>

<header class="hero">
  <div class="hero-photo" role="img" aria-label="Businessman reviewing sales charts on a tablet at his desk"></div>
  <div class="hero-shade"></div>
  <nav class="topnav">
    <div class="brand"><span class="brand-dot"></span>BRIGHTLANE PROMO WORKS</div>
    <div class="menu">
      <a class="active">Home</a><a>Our Incentives</a><a>Sample</a><a>How it works</a><a>Testimonials</a><a>FAQ</a><a>Contact</a><a>Login</a>
    </div>
  </nav>
  <div class="contact-line"><span>&#9742; International: 1-800-555-0142</span><span>&#9742; USA: 555-014-7720</span></div>
  <h1 class="hero-title heading">Unlimited Incentives<br>For $99 Monthly - No Contracts<br>30 Day Risk Free Trial</h1>
  <div class="hero-actions"><a class="btn btn-white">Learn More</a><a class="btn btn-blue">Sign Up Risk free for 30 days!</a></div>
</header>

<section class="incentives">
  <h2 class="heading">Create Promotional Giveaways Using Any Of These Incentives!</h2>
  <div class="cards">
    <div class="card c1">
      <div class="img" role="img" aria-label="Tropical resort at dusk"></div><div class="veil"></div>
      <h3>Vacation Getaways</h3>
      <p><b>3-7 Nights Including Airfare</b><br>Up To $2000 Value<br>Your customers just pay taxes!</p>
      <a class="more">More Details &rarr;</a>
    </div>
    <div class="card c2"><div class="img" role="img" aria-label="Cruise ship on open sea"></div><div class="veil"></div><h3>Cruise Getaways</h3></div>
    <div class="card c3"><div class="img" role="img" aria-label="Couple enjoying a new tablet"></div><div class="veil"></div><h3>Electronic Product Giveaways</h3></div>
    <div class="card c4"><div class="img" role="img" aria-label="Fuel pump at a gas station"></div><div class="veil"></div><h3>Gas Reward Incentives</h3></div>
    <div class="card c5"><div class="img" role="img" aria-label="Shopper with grocery bags"></div><div class="veil"></div><h3>Grocery Reward Incentives</h3></div>
  </div>
</section>

<section class="stats">
  <div class="stat" style="left:105px"><strong>4</strong><span>Years In Business</span></div>
  <div class="stat" style="left:366px"><strong>13,000+</strong><span>Clients Enrolled</span></div>
  <div class="stat" style="left:609px"><strong>2</strong><span>Million Certificates in Circulation</span></div>
  <div class="stat" style="left:845px"><strong>170,000+</strong><span>Redemptions To Date</span></div>
</section>

<section class="wing">
  <div class="wing-photo" role="img" aria-label="Airplane wing above the clouds at sunset"></div>
  <div class="wing-copy">
    <h2 class="heading">Increase Leads &amp; Sales From Your Existing Marketing Efforts By Offering High Perceived Value Incentives To Your Customers!</h2>
    <p>Create a variety of giveaway promotions for your business with an unlimited supply of top quality vacation getaway certificates, restaurant gift certificates, electronic product giveaways and gas or grocery rewards for just $99/month.</p>
    <p class="strong">Whether you need 100 or 100,000 you will never pay more than $99.</p>
    <a class="btn">Learn More</a>
  </div>
</section>

<section class="plugin">
  <h2 class="heading">We plug right into your existing business model in 4 ways</h2>
  <div class="tile" style="top:167px;left:100px"><h3>Advertising</h3><p>Boost response rates from your existing ads by adding one extra tagline "Call for a Free Quote and receive 3 Free Nights at a popular destination, No Purchase Necessary!" and watch how many more leads you could generate.</p></div>
  <div class="tile" style="top:167px;left:466px"><h3>Residual Business</h3><p>Remind past clients about your products &amp; services with a 2 Night Hotel Stay for previous buyers, using a personal touch and an incentive to return.</p></div>
  <div class="tile" style="top:306px;left:100px"><h3>Sales</h3><p>Now that you have generated the lead, try enticing a prospect with an upgrade to a three night getaway if they purchase today. There are so many ways to clinch a deal by offering our incentives as a reward in your closing question.</p></div>
  <div class="tile" style="top:306px;left:466px"><h3>Referrals</h3><p>Contact all of your past customers and offer a deluxe vacation package to anyone who fulfills your request for a new referral. Or, at the end of your sales presentation, offer your incentive for a friendly referral.</p></div>
  <div class="phone-mock"><div class="phone-screen" role="img" aria-label="Phone screen showing a city lights vacation promotion"></div></div>
</section>

<section class="distribution">
  <h2 class="heading">Easy Distribution</h2>
  <div class="channel" style="left:104px">
    <svg width="52" height="48" viewBox="0 0 52 48" fill="#fff"><rect x="13" y="2" width="26" height="12"/><rect x="2" y="16" width="48" height="20" rx="3"/><rect x="13" y="30" width="26" height="16" fill="#fff" stroke="#1370e0" stroke-width="3"/></svg>
    <h3>Print</h3><p>Download PDF certificates to print and physically hand them out or mail them to your customers.</p>
  </div>
  <div class="channel" style="left:362px">
    <svg width="56" height="48" viewBox="0 0 56 48"><rect x="2" y="6" width="52" height="36" fill="#fff"/><path d="M3 8 L28 28 L53 8" fill="none" stroke="#1370e0" stroke-width="3"/></svg>
    <h3>Email</h3><p>Email e-certificates to your customers individually or in bulk with just one click after your closing question.</p>
  </div>
  <div class="channel" style="left:614px">
    <svg width="56" height="48" viewBox="0 0 56 48"><rect x="3" y="3" width="50" height="32" fill="none" stroke="#fff" stroke-width="4"/><rect x="22" y="35" width="12" height="7" fill="#fff"/><rect x="14" y="42" width="28" height="4" fill="#fff"/></svg>
    <h3>Online Automation</h3><p>Add our web banners on your website. Your customers click on the banner to get their certificate.</p>
  </div>
  <div class="channel" style="left:876px">
    <svg width="52" height="48" viewBox="0 0 52 48" fill="#fff"><path d="M4 4 H48 V34 H20 L8 44 V34 H4 Z"/><circle cx="16" cy="19" r="3" fill="#1370e0"/><circle cx="26" cy="19" r="3" fill="#1370e0"/><circle cx="36" cy="19" r="3" fill="#1370e0"/></svg>
    <h3>SMS</h3><p>Send one certificate through text messaging with just one click. Coming Soon!</p>
  </div>
</section>

<section class="gift">
  <div class="gift-photo" role="img" aria-label="Wrapped gift box with a teal ribbon on a dark wooden table"></div>
  <div class="gift-copy">
    <h2 class="heading">Give away an unlimited amount of certificates to your customers for just $99 bucks a month.</h2>
    <p>We are A rated with the Regional Business Review Board as well as a licensed seller of travel registered with the State Seller of Travel Registry. We also participate in The Traveler Protection Trust (TPT) which was created to protect consumers from unscrupulous travel companies.</p>
    <div class="gift-actions"><a class="btn">Read More</a><a class="link">Sign Up Now Risk Free for 30 Days &rarr;</a></div>
  </div>
</section>

<section class="support">
  <div class="scard s1" style="left:100px">
    <div class="img" role="img" aria-label="Laptop on a desk"></div>
    <div class="panel">
      <h3>Completely Separate Redemption Websites - Online Redemption/Reservation Requests</h3>
      <p>First and foremost we're a marketing company and we will protect the integrity of your promotions. By using separate redemption websites we keep your customers from finding out what a great value you are getting.</p>
      <a>Read More &rarr;</a>
    </div>
  </div>
  <div class="scard s2" style="left:444px">
    <div class="img" role="img" aria-label="Customer service agent with a headset"></div>
    <div class="caption">Top Notch Customer Service With Superior Member Support</div>
  </div>
  <div class="scard s3" style="left:788px">
    <div class="img" role="img" aria-label="Person thinking at a desk"></div>
    <div class="caption">Too good to be true! How Do We Do It?</div>
  </div>
</section>

<section class="sales">
  <div class="sales-photo" role="img" aria-label="Red telephone handset on a white background"></div>
  <div class="sales-copy">
    <h2 class="heading">Increase your sales.<br>Improve your customer services.</h2>
    <div class="sales-links"><a>Watch video to save 20% today</a><a>Take a quick tour to our incentives</a><a>View Redeem Samples</a></div>
  </div>
</section>

<section class="reseller">
  <div class="reseller-photo" role="img" aria-label="Business team meeting in a bright office"></div>
  <h2 class="heading">Know Any Businesses That Could Benefit Using Incentives To Bring In More Customers?</h2>
  <a>Click Here To Learn More About Our Reseller Program</a>
</section>

<footer class="site-footer">
  <ul class="fcol" style="left:100px"><li><h4>Home</h4></li><li>Our Incentives</li><li>Sample</li><li>How it works</li><li>Testimonials</li><li>FAQ</li><li>Contact</li></ul>
  <ul class="fcol" style="left:220px"><li><h4>Advertising</h4></li><li>Residual Business</li><li>Sales</li><li>Referrals</li><li>Quick Tour</li><li>Redeem Samples</li><li>Watch Video</li></ul>
  <ul class="fcol" style="left:372px"><li><h4>Download Brochure</h4></li><li>Reseller Program</li><li>Terms &amp; Conditions</li><li>Privacy Policy</li><li>Login</li></ul>
  <ul class="fcol" style="left:535px"><li><h4>Follow Us</h4></li><li><span class="ico"></span>Social Page</li><li><span class="ico"></span>News Feed</li><li><span class="ico"></span>Video Channel</li></ul>
  <ul class="fcol" style="left:645px"><li><h4>Contact Us</h4></li><li>&#9742; International: 1-800-555-0142</li><li>&#9742; USA: 555-014-7720</li><li>hello@brightlanepromoworks.biz</li><li>support@brightlanepromoworks.biz</li></ul>
  <ul class="fcol" style="left:945px;width:160px"><li><h4>About Us</h4></li><li>We are A rated with the Regional Business Review Board as well as a licensed seller of travel registered with the State Seller of Travel Registry. We also participate in The Traveler Protection Trust.</li></ul>
  <div class="copyright">&copy; 2010-2018 Brightlane Promo Works Group, Inc. - All Rights Reserved. Affiliate Program.</div>
</footer>

</body>
</html>
```